Modern & Fresh Sumeray Book Cover

Need a creative e-book cover for my book.

Title: Get Sumeray Sorted
Subtitle: Learn How To Easily Choose & Enroll in the Perfect Coverage at the Perfect Time.

Target Market(s)

60-70 year olds in the United States

Font styles to use
Sans Serif

Colors
9bcb3c
33a6d7

Requirements
Must have
• Must look modern and fresh.
• Use our company colors www.BrovaMint.com

```html
<!DOCTYPE html>
<html lang="en">
<head>
<meta charset="utf-8">
<title>Get Sumeray Sorted — Book Cover</title>
<link rel="stylesheet" href="https://fonts.googleapis.com/css2?family=Ubuntu:wght@400;500;700&display=swap">
<style>
  :root {
    --green-light: #8dc63f;
    --green-dark: #5b9130;
    --blue-light: #12aee0;
    --blue-dark: #3a4ea2;
    --navy-text: #2f4497;
    --accent-green: #8cc43e;
    --page: #ffffff;
  }
  html, body {
    margin: 0;
    padding: 0;
    overflow: hidden;
    background: var(--page);
  }
  .cover {
    position: relative;
    width: 776px;
    height: 1200px;
    background: var(--page);
    overflow: hidden;
    font-family: "Ubuntu", sans-serif;
  }
  .title {
    margin: 0;
    position: absolute;
    left: 0;
    right: 0;
    top: 48px;
    text-align: center;
    font-weight: 700;
  }
  .title-lead {
    display: block;
    font-size: 118px;
    line-height: 140px;
    letter-spacing: -1px;
    background: linear-gradient(180deg, var(--green-light) 20%, var(--green-dark) 100%);
    -webkit-background-clip: text;
    background-clip: text;
    color: transparent;
  }
  .title-main {
    display: block;
    margin-top: 10px;
    font-size: 232px;
    font-weight: 500;
    line-height: 270px;
    letter-spacing: -4px;
    background: linear-gradient(180deg, var(--blue-light) 25%, var(--blue-dark) 90%);
    -webkit-background-clip: text;
    background-clip: text;
    color: transparent;
  }
  .subtitle {
    position: absolute;
    left: 0;
    right: 0;
    top: 536px;
    margin: 0;
    text-align: center;
    font-size: 25px;
    line-height: 35px;
    color: var(--navy-text);
    font-weight: 400;
  }
  .subtitle .highlight {
    color: var(--accent-green);
    font-weight: 700;
  }
  .emblem-area {
    position: absolute;
    left: 148px;
    top: 676px;
    width: 484px;
    height: 470px;
    border-radius: 50% 50% 44% 44%;
    background: linear-gradient(180deg, #c9e59f 0%, #a9dbef 60%, #9fb0dc 100%);
    opacity: 0.7;
  }
</style>
</head>
<body>
  <main class="cover">
    <h1 class="title">
      <span class="title-lead">Get Sumeray</span>
      <span class="title-main">Sorted</span>
    </h1>
    <p class="subtitle">
      Learn How To Easily <span class="highlight">Choose</span> and <span class="highlight">Enroll</span><br>
      in the Perfect Coverage at the Perfect Time.
    </p>
    <div class="emblem-area" role="img" aria-label="Emblem illustration: a figure with raised arms inside a glowing lightbulb shape, in green and blue"></div>
  </main>
</body>
</html>
```